Brellin Trade Partners - we are Asian sourcing agents

We are sourcing agents based in the USA and we act as sourcing agents for clients in throughout the world. We focus primarily on custom sewn goods. So basically companies who do not have the in-house expertise to do it themselves, come to us and have us find suitable factories in Asia to do the production. We are middlemen. We find the factories...quote the project...manage the quality control and then deliver the goods directly to our customer's door. We pride ourselves in making the communication very easy and precise.

Current page is www.brellintrade.example

I am not happy w/ the overall look. The spacing...the photos, the fonts...the design elements...the pictures. I want a cool, crisp design that conveys professionalism and clearly depicts/explains what we do.

Requirements
Must have
• use my logo....I like it...it was designed by someone on this website.
Nice to have
• a video/animation of the entire process would be wonderful. Showing initial contact with our office in the USA...then to my correspondence with my offices in Taiwan and in Hong Kong...and then back and fort w/ the customer.....and then between my people in Hong Kong/Taiwan with the local factories......and then a quote is generated and sent to my client......to samples being made and sent for approval.....to a PO being generated......to final samples being sent.....to the order being shipped and delivered to the clients warehouse. I was thinking of an animation showing arrows and text showing the back and forth communication and explaining how the process flows.

```html
<!DOCTYPE html>
<html lang="en">
<head>
<meta charset="utf-8">
<title>Brellin Trade Partners</title>
<link rel="stylesheet" href="https://fonts.googleapis.com/css2?family=Jost:wght@300;400;500;600;700&display=swap">
<style>
:root{
  --navy:#283a6e;
  --green:#8db26a;
  --text:#6e6e6e;
  --dark-btn:#4b4b4b;
  --grey-band:#ececec;
  --card:#ffffff;
  --footer:#2f2f2f;
  --footer-base:#272727;
  --footer-text:#8d8d8d;
  --line:#3d3d3d;
}
*{box-sizing:border-box;margin:0;padding:0}
html,body{width:1200px;height:2898px;overflow:hidden}
body{font-family:"Jost",sans-serif;color:var(--text);background:#fff;position:relative}
.wrap{position:absolute;left:148px;width:904px}

/* header */
.header{position:absolute;top:0;left:0;width:1200px;height:145px;background:#fff}
.social{position:absolute;right:148px;top:22px;display:flex;gap:12px}
.social span{width:12px;height:12px;border-radius:50%;background:#c9c9c9;display:block}
.topbar{position:absolute;left:168px;top:50px;font-size:11px;color:#555;display:flex;gap:18px;align-items:center}
.topbar .item{display:flex;align-items:center;gap:6px}
.logo{position:absolute;left:148px;top:78px;display:flex;align-items:center;gap:8px}
.logo .mark{width:34px;height:34px;border-radius:50%;background:var(--green)}
.logo .name{font-size:13px;font-weight:600;color:var(--navy);line-height:15px;letter-spacing:.3px}
.nav{position:absolute;right:148px;top:88px;display:flex;gap:30px;font-size:13px;font-weight:500;letter-spacing:.9px;color:#333}
.nav .active{color:var(--green)}

/* hero */
.hero{position:absolute;top:145px;left:0;width:1200px;height:508px;background:linear-gradient(160deg,#2a241f 0%,#5a5047 35%,#3e3731 65%,#1e1a17 100%);overflow:hidden}
.hero-photo{position:absolute;inset:0}
.hero h1{position:absolute;top:195px;width:100%;text-align:center;color:#fff;font-weight:300;font-size:40px;line-height:44px}
.hero h2{position:absolute;top:247px;width:100%;text-align:center;color:#fff;font-weight:700;font-size:44px;line-height:48px;letter-spacing:.5px}
.hero .cta{position:absolute;left:415px;top:337px;width:370px;height:51px;background:var(--green);color:#fff;font-size:21px;display:flex;align-items:center;justify-content:center}
.hero .dots{position:absolute;top:483px;left:555px;display:flex;gap:8px;align-items:center}
.hero .dots span{width:8px;height:8px;border-radius:50%;border:1.5px solid #fff}
.hero .dots span.on{background:#fff}

/* welcome */
.welcome{top:686px;text-align:center}
.welcome h3{font-size:31px;font-weight:400;color:var(--navy)}
.welcome p{margin:18px auto 0;width:830px;font-size:15px;line-height:25px;color:#777}
.btn-dark{display:inline-block;margin-top:34px;width:208px;height:49px;line-height:49px;background:var(--dark-btn);color:#fff;font-size:14px;font-weight:600}

/* solutions */
.band{position:absolute;top:1080px;left:0;width:1200px;height:1048px;background:var(--grey-band)}
.solutions{top:1127px}
.solutions h3{font-size:31px;font-weight:400;color:#333}
.solutions .lead{margin-top:16px;font-size:16px;line-height:24px;color:#777}
.filters{margin-top:22px;display:flex;gap:8px}
.filters span{font-size:11px;padding:4px 9px;border:1px solid #d5d5d5;border-radius:3px;color:#888}
.filters span.on{background:#fff;color:#333;border-color:#fff}
.grid{position:absolute;top:230px;left:0;display:grid;grid-template-columns:repeat(4,210px);column-gap:21px;row-gap:21px}
.card{background:var(--card);height:339px}
.card .ph{height:170px}
.card h4{margin:15px 14px 0;font-size:14px;font-weight:600;color:var(--navy)}
.card p{margin:8px 14px 0;font-size:11px;line-height:16px;color:#777}

/* find us */
.find{top:2180px}
.find .col{position:absolute;top:0}
.find h3{font-size:31px;font-weight:400;color:#333}
.find p{margin-top:20px;width:440px;font-size:13px;line-height:20px;color:#666}
.contact-line{display:flex;align-items:center;gap:10px;font-size:12px;color:#666;margin-top:12px}
.map{position:absolute;left:468px;top:51px;width:434px;height:234px;background:linear-gradient(135deg,#e6e4df,#d9d6cf 50%,#e9e7e2)}

/* footer */
.footer{position:absolute;top:2527px;left:0;width:1200px;height:318px;background:var(--footer)}
.fcol{position:absolute;top:38px}
.fcol h5{font-size:17px;font-weight:400;color:#e2e2e2;line-height:22px}
.fcol p{font-size:11px;line-height:15px;color:var(--footer-text);margin-top:14px;width:175px}
.list{margin-top:20px;width:210px}
.list li{list-style:none;font-size:12px;color:#bfbfbf;padding:10px 0;border-bottom:1px solid var(--line)}
.news{margin-top:26px;width:200px}
.news .n{padding-bottom:14px;border-bottom:1px solid var(--line);margin-bottom:14px}
.news .t{font-size:12px;color:#c4c4c4;line-height:16px}
.news .d{font-size:11px;color:#7a7a7a;margin-top:6px}
.base{position:absolute;top:2845px;left:0;width:1200px;height:53px;background:var(--footer-base);font-size:11px;color:#9a9a9a}
.base .copy{position:absolute;left:152px;top:20px}
.base .info{position:absolute;right:150px;top:20px;display:flex;gap:20px}
.base .info span{display:flex;gap:6px;align-items:center}
</style>
</head>
<body>

<header class="header">
  <div class="social"><span></span><span></span><span></span><span></span><span></span></div>
  <div class="topbar">
    <span class="item"><svg width="10" height="10" viewBox="0 0 10 10"><path d="M2 1l2 2-1 1.5c.6 1.2 1.4 2 2.5 2.5L7 6l2 2-1.5 1.5C4.5 9 1 5.5.5 2.5z" fill="#555"/></svg>123 456 789</span>
    <span class="item"><svg width="11" height="8" viewBox="0 0 11 8"><rect width="11" height="8" fill="#555"/><path d="M0 0l5.5 4.5L11 0" stroke="#fff" fill="none"/></svg>support@brellintrade.example</span>
    <span class="item"><b style="color:#555">?</b>Frequently Asked Questions</span>
  </div>
  <div class="logo"><span class="mark"></span><span class="name">BRELLIN TRADE<br>PARTNERS</span></div>
  <nav class="nav"><span class="active">HOME</span><span>ABOUT</span><span>SOURCING SOLUTIONS</span><span>REQUEST A QUOTE</span><span>CONTACT</span></nav>
</header>

<section class="hero">
  <div class="hero-photo" role="img" aria-label="Close-up of a sewing machine presser foot stitching dark fabric"></div>
  <h1>Business is risky.</h1>
  <h2>DON’T GET AT IT ALONE.</h2>
  <div class="cta">Request your free quote now</div>
  <div class="dots"><span class="on"></span><span></span><span></span><span></span></div>
</section>

<section class="wrap welcome">
  <h3>Welcome to Brellin Trade Partners</h3>
  <p>Brellin Trade Partners has been sourcing custom sewn goods in Asia since 1998. We work with our clients by matching their unique production needs with the best possible China sewing factories. We manage the entire process from start to finish, by first identifying the best factories to quote each job. The next step is negotiating the best (fair) price possible. We complete the process by monitoring the quality of the goods during production, and then managing the ocean logistics, customs clearances and local delivery right to your door. Our services and our total commitment to customer satisfaction help level the playing field by giving our customers access to low cost, high quality China contract sewing.</p>
  <span class="btn-dark">Know more about us</span>
</section>

<div class="band"></div>
<section class="wrap solutions">
  <h3>Sourcing solutions</h3>
  <p class="lead">We outsource sewing services direct from China. Our long-established and extensive network of offshore factory-partners provides our clients with access to a wide variety of contract sewing expertise from Chinese manufacturers. Clients only need to communicate with our US agents, but will have the benefits of the cost savings &amp; quality workmanship from offshore outsourcing from Asia.</p>
  <div class="filters"><span class="on">All</span><span>Bags &amp; gloves</span><span>Cases</span><span>Sporting goods</span><span>Medical</span><span>Sewn goods</span></div>
  <div class="grid">
    <article class="card"><div class="ph" role="img" aria-label="Black messenger bag" style="background:linear-gradient(#f4f4f4,#d8d8d8)"></div><h4>Custom Bag Manufacturer</h4><p>We can accommodate any material request that you may have – leather, polyester, nylon, PVC, cotton or canvas. Packaging can be for individual retail sales or bulk packing.</p></article>
    <article class="card"><div class="ph" role="img" aria-label="Black cosmetic case" style="background:linear-gradient(#f6f6f6,#d5d5d5)"></div><h4>Custom Cosmetic Case</h4><p>We can accommodate any material request that you may have – leather, polyester, nylon, PVC, cotton or canvas. Packaging can be for individual retail sales or bulk packing.</p></article>
    <article class="card"><div class="ph" role="img" aria-label="Pair of black ski gloves" style="background:linear-gradient(#f5f5f5,#d3d3d3)"></div><h4>Custom Ski Glove</h4><p>We can accommodate any material request that you may have – leather, polyester, nylon, PVC, cotton or canvas. Packaging can be for individual retail sales or bulk packing.</p></article>
    <article class="card"><div class="ph" role="img" aria-label="Green oxygen tank in a carry bag" style="background:linear-gradient(#f4f6f4,#d4ddd6)"></div><h4>Oxygen Tank Cases &amp; Bags</h4><p>We can accommodate any material request that you may have – leather, polyester, nylon, PVC, cotton or canvas. Packaging can be for individual retail sales or bulk packing.</p></article>
    <article class="card"><div class="ph" role="img" aria-label="Blue pet collar and harness" style="background:linear-gradient(#f5f6f9,#d7dde8)"></div><h4>Pet Collars</h4><p>We can accommodate any material request that you may have – leather, polyester, nylon, PVC, cotton or canvas. Packaging can be for individual retail sales or bulk packing.</p></article>
    <article class="card"><div class="ph" role="img" aria-label="Blue yoga mat in a grey carry bag" style="background:linear-gradient(#f5f6f8,#d2d8de)"></div><h4>Yoga Gear &amp; Accessories</h4><p>We can accommodate any material request that you may have – leather, polyester, nylon, PVC, cotton or canvas. Packaging can be for individual retail sales or bulk packing.</p></article>
    <article class="card"><div class="ph" role="img" aria-label="Blue cover over a motorcycle" style="background:linear-gradient(#f4f5f9,#cdd3e4)"></div><h4>Cover Materials</h4><p>We can accommodate any material request that you may have – leather, polyester, nylon, PVC, cotton or canvas. Packaging can be for individual retail sales or bulk packing.</p></article>
    <article class="card"><div class="ph" role="img" aria-label="Stack of cardboard shipping boxes" style="background:linear-gradient(#f8f5f0,#dccbb0)"></div><h4>Packaging</h4><p>We can accommodate any material request that you may have – leather, polyester, nylon, PVC, cotton or canvas. Packaging can be for individual retail sales or bulk packing.</p></article>
  </div>
</section>

<section class="wrap find">
  <div class="col" style="left:4px">
    <h3>Where to find us ?</h3>
    <p>Because we act as agents for dozens of clients, we can most often get the best pricing because of our combined group buying power. We are also wise to the many pitfalls that can arise when an inexperienced buyer with no local representation tries to deal directly with an Asian factory. Don’t go at it alone – trust Brellin Trade Partners for your outsourced needs. You’ll get the best pricing, better service and most of all, peace of mind.</p>
    <div class="contact-line" style="margin-top:22px"><svg width="11" height="8" viewBox="0 0 11 8"><rect width="11" height="8" fill="#777"/><path d="M0 0l5.5 4.5L11 0" stroke="#fff" fill="none"/></svg>Email: support@brellintrade.example</div>
    <div class="contact-line"><svg width="11" height="10" viewBox="0 0 11 10"><rect x="0" y="2" width="11" height="8" rx="1" fill="#777"/><rect x="3" y="0" width="5" height="3" fill="#777"/></svg>Phone: 123 456 789</div>
    <div class="contact-line"><svg width="9" height="12" viewBox="0 0 9 12"><path d="M4.5 0A4.5 4.5 0 0 0 0 4.5C0 8 4.5 12 4.5 12S9 8 9 4.5A4.5 4.5 0 0 0 4.5 0z" fill="#777"/><circle cx="4.5" cy="4.5" r="1.6" fill="#fff"/></svg>12 Harbor Lane, Unit B-4 - Exeter, NH 03833</div>
  </div>
  <div class="col" style="left:468px"><h3>Our Location</h3></div>
  <div class="map" role="img" aria-label="Street map showing the office location"></div>
</section>

<footer class="footer">
  <div class="fcol" style="left:152px">
    <h5>Brellin Trade<br>Partners, LLC</h5>
    <p>Our US headquarters is in New Hampshire, and we also have a buying office in Hong Kong that is managed by local Chinese residents who are experts in textiles and sewn goods production.</p>
    <p>Our Hong Kong management is able to negotiate the best pricing with the China factories, to handle disputes, and to fully understand the many nuances involved in working with a China factory. This simply cannot be effectively managed from the USA.</p>
  </div>
  <div class="fcol" style="left:381px">
    <h5>Products solutions</h5>
    <ul class="list"><li>Custom bags &amp; gloves</li><li>Cases</li><li>Sporting goods</li><li>Sewn goods</li><li>Medical</li><li>Accessories</li></ul>
  </div>
  <div class="fcol" style="left:612px">
    <h5>News</h5>
    <div class="news">
      <div class="n"><div class="t">Brellin’s new partnership<br>in Barcelona</div><div class="d">April, 2015</div></div>
      <div class="n"><div class="t">Brellin’s Hong Kong office<br>receive a local Award</div><div class="d">March, 2015</div></div>
    </div>
  </div>
</footer>
<div class="base">
  <span class="copy">Copyright 2015 - All Rights Reserved</span>
  <div class="info"><span>123 456 789</span><span>support@brellintrade.example</span><span>? Frequently Asked Questions</span></div>
</div>

</body>
</html>
```